Letterhead for a German Distribution/Manufacturing Company

We need a professional Letterhead in a unique Design.
not to playful.
The Letterhead has to show show that we are a international company with headquater in Germany.
all details like adress, Vat Tax Number, Bank Accout, Eori, email, Company number has to be on the Letterhead.
for example use: VAT TAX DE5704168 Bank Account: Norrfeld Bank IBAN DE421705238ß310482 Swift: KOLV3154802 EORI 3041296587 Company Number: HRB 61508 Adress: VOLTRINA UG Amsel Strasse 7 Postal Code 04683 City Erlenbrück Country: Germany Email: info@voltrina-example.com
the design can be colored but doesnt have to be
Industry/Entity Type
Manufacturing and international distribution
Requirements
Must have
- show that we are a international company with headquater in Germany. our company infos and logo

```html
<!DOCTYPE html>
<html lang="en">
<head>
<meta charset="utf-8">
<title>VOLTRINA UG – Letterhead</title>
<link rel="stylesheet" href="https://fonts.googleapis.com/css2?family=Poppins:wght@300;400;600;700&display=swap">
<style>
  :root {
    --ink: #333333;
    --paper: #ffffff;
    --mist-light: #f7f8f9;
    --mist-dark: #e3e4e6;
    --rule: #4a4a4a;
  }
  * { box-sizing: border-box; margin: 0; padding: 0; }
  html, body { width: 856px; height: 1200px; overflow: hidden; background: var(--paper); }
  body { font-family: 'Poppins', sans-serif; color: var(--ink); }
  .letterhead { position: relative; width: 856px; height: 1200px; overflow: hidden; background: var(--paper); }

  .footer-backdrop {
    position: absolute; left: 0; right: 0; top: 910px; bottom: 0;
    background: linear-gradient(180deg, rgba(247,248,249,0) 0%, var(--mist-light) 18%, var(--mist-dark) 55%, var(--mist-light) 100%);
  }

  .brand {
    position: absolute; top: 124px; left: 0; width: 856px;
    display: flex; justify-content: center; align-items: center; gap: 16px;
  }
  .brand-dot { width: 42px; height: 42px; border-radius: 50%; background: var(--ink); }
  .brand-name { font-weight: 600; font-size: 54px; letter-spacing: 1px; line-height: 1; color: var(--ink); }

  .sender { position: absolute; left: 110px; top: 262px; }
  .sender-name { font-weight: 700; font-size: 22px; line-height: 1.2; margin-bottom: 6px; }
  .sender-line { font-size: 12.5px; line-height: 17.9px; font-weight: 400; }

  .letter-date { position: absolute; right: 108px; top: 259px; font-size: 13.5px; }

  .letter-body { position: absolute; left: 110px; top: 436px; width: 636px; }
  .letter-body p { font-size: 12.7px; line-height: 17.9px; text-align: justify; margin-bottom: 17.9px; }

  .signature { position: absolute; right: 111px; top: 890px; text-align: right; }
  .signature-role { font-weight: 700; font-size: 14.5px; line-height: 1.4; }
  .signature-line { font-size: 12.8px; line-height: 19px; }

  .company-details { position: absolute; left: 71px; top: 1068px; width: 714px; display: flex; }
  .detail-column { flex: 1; text-align: center; }
  .detail-column + .detail-column { border-left: 1px solid var(--rule); }
  .detail-title { font-weight: 600; font-size: 14px; line-height: 1; margin-bottom: 14px; }
  .detail-value { font-weight: 300; font-size: 12.5px; line-height: 19.5px; }
</style>
</head>
<body>
<div class="letterhead">
  <div class="footer-backdrop" role="img" aria-label="Soft grey backdrop of overlapping pale squares behind the footer"></div>

  <header class="brand">
    <span class="brand-dot"></span>
    <span class="brand-name">VOLTRINA</span>
  </header>

  <section class="sender">
    <h1 class="sender-name">Name Surname</h1>
    <p class="sender-line">VOLTRINA UG Amsel Strasse 7, 04683, Erlenbrück, Germany</p>
    <p class="sender-line">info@voltrina-example.com</p>
    <p class="sender-line">HRB 61508</p>
    <p class="sender-line">04683</p>
  </section>

  <p class="letter-date">Date, 10 September, 2030</p>

  <main class="letter-body">
    <p>Lorem ipsum dolor sit amet, consectetur adipisicing elit, sed do eiusmod tempor incididunt ut labore et dolore magna aliqua. Ut enim ad minim veniam, quis nostrud exercitation ullamco laboris nisi ut aliquip ex ea commodo consequat. Duis aute irure dolor in reprehenderit in voluptate velit esse cillum dolore eu fugiat nulla pariatur. Excepteur sint occaecat cupidatat non proident, sunt in culpa qui officia deserunt mollit anim id est laborum. Sed ut perspiciatis unde omnis iste natus error sit voluptatem accusantium doloremque laudantium, totam rem aperiam, eaque ipsa quae ab illo inventore veritatis et quasi architecto beatae vitae dicta sunt explicabo. Nemo enim ipsam voluptatem quia voluptas sit aspernatur aut odit aut fugit, sed quia consequuntur magni dolores eos qui ratione voluptatem sequi nesciunt. Neque porro voluptatem sequi nesciunt. Nemo enim ipsam voluptatem quia voluptas.</p>
    <p>Lorem ipsum dolor sit amet, consectetur adipisicing elit, sed do eiusmod tempor incididunt ut labore et dolore magna aliqua. Ut enim ad minim veniam, quis nostrud exercitation ullamco laboris nisi ut aliquip ex ea commodo consequat. Duis aute irure dolor in reprehenderit in voluptate velit esse cillum dolore eu fugiat nulla pariatur. Excepteur sint occaecat cupidatat non proident, sunt in culpa qui officia deserunt mollit anim id est laborum. Sed ut perspiciatis unde omnis iste natus error sit voluptatem accusantium doloremque laudantium, totam rem aperiam, eaque ipsa quae ab illo inventore veritatis et quasi architecto beatae vitae dicta sunt explicabo. Nemo enim ipsam voluptatem quia voluptas sit aspernatur aut odit aut.</p>
    <p>Lorem ipsum dolor sit amet, consectetur adipisicing elit, sed do eiusmod tempor incididunt ut labore et dolore magna aliqua. Ut enim ad minim veniam, quis nostrud exercitation ullamco laboris nisi ut aliquip ex ea commodo consequat. .</p>
  </main>

  <section class="signature">
    <p class="signature-role">Position</p>
    <p class="signature-line">Name Surname</p>
    <p class="signature-line">Website</p>
  </section>

  <footer class="company-details">
    <div class="detail-column">
      <p class="detail-title">Vat Tax &amp; EORI</p>
      <p class="detail-value">DE5704168</p>
      <p class="detail-value">3041296587</p>
    </div>
    <div class="detail-column">
      <p class="detail-title">Bank Account</p>
      <p class="detail-value">Norrfeld Bank IBAN</p>
      <p class="detail-value">DE421705238ß310482</p>
    </div>
    <div class="detail-column">
      <p class="detail-title">Swift</p>
      <p class="detail-value">KOLV3154802</p>
    </div>
  </footer>
</div>
</body>
</html>
```